23rd Annual Harrowgate Lantern Film Festival Poster

Design an eye catchy, stylish poster for our 23rd film festival. Be different not just a poster with a film reel. Think outside of the box with a design that will attract peoples attention. Colorful (you choose the colors). Make it fun and creative, like the film festival. Show your talents in the design. Be sure it is new and stylish. Dates are August 21 - 29, 2020. Poster size will be 27 inches by 40 inches

Target Market(s)

Upper Middle class - movie lovers

Font styles to use
Sans Serif

Colors
33a6d7

Requirements
Must have
• NO CLIP ART - be original !
Nice to have
• abstract - think outside the box
Should not have
• CLIP ART

```html
<!DOCTYPE html>
<html lang="en">
<head>
<meta charset="utf-8">
<title>23rd Annual Harrowgate Lantern Film Festival</title>
<link rel="stylesheet" href="https://fonts.googleapis.com/css2?family=Audiowide&display=swap">
<style>
  :root {
    --festival-blue: #33a6d7;
    --deep-blue: #1b3f9a;
    --navy: #0f2a6b;
    --teal: #2bb3b8;
    --paint-red: #d8321f;
    --orange: #e8612a;
    --paper-white: #f3f5f7;
    --ink-white: #ffffff;
  }
  * { margin: 0; padding: 0; box-sizing: border-box; }
  html, body {
    width: 811px;
    height: 1200px;
    overflow: hidden;
    background: var(--paper-white);
  }
  .poster {
    position: relative;
    width: 811px;
    height: 1200px;
    overflow: hidden;
    font-family: "Audiowide", sans-serif;
  }
  .painted-backdrop {
    position: absolute;
    inset: 0;
    background:
      radial-gradient(ellipse 260px 200px at 720px 150px, var(--paint-red) 0%, rgba(216,50,31,0) 75%),
      radial-gradient(ellipse 300px 180px at 560px 140px, var(--navy) 0%, rgba(15,42,107,0) 80%),
      radial-gradient(ellipse 280px 220px at 120px 120px, var(--festival-blue) 0%, rgba(51,166,215,0) 80%),
      radial-gradient(ellipse 340px 110px at 420px 500px, var(--paper-white) 0%, rgba(243,245,247,0) 90%),
      radial-gradient(ellipse 220px 260px at 80px 780px, var(--paint-red) 0%, rgba(216,50,31,0) 80%),
      radial-gradient(ellipse 240px 300px at 740px 820px, var(--paint-red) 0%, rgba(216,50,31,0) 80%),
      radial-gradient(ellipse 300px 200px at 420px 760px, var(--orange) 0%, rgba(232,97,42,0) 75%),
      radial-gradient(ellipse 320px 220px at 180px 1080px, var(--teal) 0%, rgba(43,179,184,0) 80%),
      radial-gradient(ellipse 300px 240px at 600px 1100px, var(--deep-blue) 0%, rgba(27,63,154,0) 80%),
      linear-gradient(180deg,
        var(--festival-blue) 0%,
        var(--deep-blue) 24%,
        var(--deep-blue) 34%,
        #dfe9f2 42%,
        var(--paper-white) 47%,
        #cfe4f1 53%,
        var(--festival-blue) 62%,
        var(--deep-blue) 80%,
        var(--teal) 100%);
  }
  .headline {
    position: absolute;
    left: 170px;
    width: 600px;
    text-align: center;
    white-space: nowrap;
    color: var(--ink-white);
    line-height: 1;
  }
  .edition {
    top: 212px;
    font-size: 80px;
    letter-spacing: 2px;
  }
  .festival-name {
    top: 302px;
    font-size: 21px;
    color: var(--deep-blue);
    -webkit-text-stroke: 0.6px var(--ink-white);
    letter-spacing: 0.5px;
  }
  .festival-word {
    top: 332px;
    font-size: 42px;
  }
  .festival-dates {
    top: 412px;
    font-size: 24px;
    letter-spacing: 4px;
    text-shadow: 0 0 3px rgba(15,42,107,0.6);
  }
</style>
</head>
<body>
  <main class="poster">
    <div class="painted-backdrop" role="img" aria-label="Abstract painted backdrop of blue, red, teal and white brush strokes with two cropped portrait close-ups and a small flock of birds"></div>
    <h1 class="headline edition">23RD</h1>
    <p class="headline festival-name">ANNUAL HARROWGATE LANTERN</p>
    <p class="headline festival-word">FILM FESTIVAL</p>
    <p class="headline festival-dates">AUGUST 21 - 29, 2020</p>
  </main>
</body>
</html>
```